Packaging Design for Box Containing Beautiful Copper Mugs

I need a design for a set of two 16 oz copper mugs normally used for Moscow Mules (picture attached). The box dimensions are 19 x 11 x 11 cm and it opens from the top. An example of some of the boxes the manufacturer has made in the past is attached (note: some are single, not double like I need). I would either like a "retro" like feel to the box, as it is a classic type mug from the 1950s/1960s or an "eco-feel" with matte cardboard and green/dark brown or black lettering - or get creative and see if you have a better idea! I have a logo I will need on it as well as a barcode on the bottom and the product description. It also needs to say made in India and lifetime guarantee somewhere on the box. I do have some text to add somewhere on two of the sides but the design needs to be right before I add it. So you can use a placeholder for the text and I can add it when we decide on the design. I would like it to be the kind of box you would give to a friend as a gift; As beautiful on the outside as on the inside.

Feel free to ask any questions. Thanks!

Target Market(s)

21-65 year olds who like Moscow Mules

Industry/Entity Type

Home And Garden

Font styles to use
Sans Serif

Requirements
Must have
• A design that stands apart and makes you want to grab one off the shelf and give one to a friend as a nice gift.
Nice to have
• Stylish, unique, grabs your attention

```html
<!DOCTYPE html>
<html lang="en">
<head>
<meta charset="utf-8">
<title>Hollowell Coffee Mug – Box Dieline</title>
<link rel="stylesheet" href="https://fonts.googleapis.com/css2?family=Oswald:wght@500;600&family=Sansita:wght@700&display=swap">
<style>
  :root{
    --backdrop:#5e554f;
    --board:#f7f7e8;
    --panel:#eeedda;
    --panel-light:#f4f3e4;
    --side-grey:#857c73;
    --ribbon-red:#bf3a2c;
    --badge:#dcdcc6;
    --ink:#6d6862;
    --ink-dark:#2b2724;
    --ornament:#8f877d;
    --steam:#d6d4c0;
    --fold:#d8d6c4;
  }
  html,body{margin:0;padding:0;overflow:hidden;}
  body{width:1200px;height:1200px;background:var(--backdrop);}
  .dieline{display:block;width:1200px;height:1200px;}
  .board{fill:var(--board);}
  .panel-face{fill:var(--panel);}
  .panel-shade{fill:var(--panel-light);}
  .side-band{fill:var(--side-grey);}
  .ribbon{fill:var(--ribbon-red);}
  .badge{fill:var(--badge);}
  .ornament{fill:url(#ornamentTone);}
  .divider{fill:url(#dividerTone);}
  .steam{fill:url(#steamTone);}
  .cup-body{fill:var(--ribbon-red);}
  .cup-handle{fill:none;stroke:var(--ribbon-red);stroke-width:3.4;}
  .cup-steam{fill:none;stroke:var(--ribbon-red);stroke-width:2;stroke-linecap:round;}
  .fold{stroke:var(--fold);stroke-width:.6;fill:none;}
  .brand-name{font-family:'Sansita',sans-serif;font-weight:700;fill:var(--ink-dark);text-anchor:middle;}
  .product-name{font-family:'Sansita',sans-serif;font-weight:700;fill:var(--ink);text-anchor:middle;}
  .guarantee{font-family:'Oswald',sans-serif;font-weight:600;fill:var(--board);text-anchor:middle;font-size:7px;}
  .ribbon-mark{font-family:'Oswald',sans-serif;font-weight:500;fill:var(--board);text-anchor:middle;font-size:3.6px;letter-spacing:.3px;}
  .origin{font-family:'Oswald',sans-serif;font-weight:600;fill:var(--board);font-size:8px;}
</style>
</head>
<body>
<svg class="dieline" viewBox="11 225 1000 1000" xmlns="http://www.w3.org/2000/svg">
  <defs>
    <radialGradient id="ornamentTone" cx="50%" cy="50%" r="60%">
      <stop offset="0" stop-color="#8f877d" stop-opacity=".55"/>
      <stop offset="1" stop-color="#8f877d" stop-opacity="0"/>
    </radialGradient>
    <linearGradient id="dividerTone" x1="0" x2="1">
      <stop offset="0" stop-color="#bf3a2c" stop-opacity="0"/>
      <stop offset=".5" stop-color="#bf3a2c" stop-opacity=".7"/>
      <stop offset="1" stop-color="#bf3a2c" stop-opacity="0"/>
    </linearGradient>
    <linearGradient id="steamTone" x1="0" y1="1" x2="0" y2="0">
      <stop offset="0" stop-color="#d6d4c0" stop-opacity="0"/>
      <stop offset=".45" stop-color="#d6d4c0" stop-opacity=".9"/>
      <stop offset="1" stop-color="#d6d4c0" stop-opacity=".35"/>
    </linearGradient>
  </defs>

  <!-- top lid -->
  <g class="lid">
    <path class="board" d="M262,657 L262,510 Q262,500 272,500 L490,500 Q500,500 500,510 L500,657 Z"/>
    <text class="brand-name" x="381" y="582" font-size="20">Hollowell</text>
    <rect class="divider" x="351" y="596" width="60" height="5" rx="2.5" role="img" aria-label="Small red scroll divider ornament"/>
    <text class="product-name" x="381" y="622" font-size="14">Coffee Mug</text>
  </g>

  <!-- dust flaps -->
  <rect class="board" x="122" y="590" width="140" height="67"/>
  <rect class="board" x="500" y="590" width="140" height="67"/>

  <!-- left side panel -->
  <rect class="side-band" x="122" y="657" width="140" height="140"/>
  <polygon class="board" points="122,797 262,797 262,865 152,865 122,822"/>

  <!-- front panel -->
  <g class="front-panel">
    <rect class="panel-face" x="262" y="657" width="238" height="140"/>
    <polygon class="panel-shade" points="410,797 500,727 500,797"/>
    <ellipse class="steam" cx="440" cy="708" rx="30" ry="42" role="img" aria-label="Faint rising steam decoration"/>
    <path class="ribbon" d="M363,657 H401 V756 L382,750 L363,756 Z"/>
    <text class="ribbon-mark" x="382" y="664">• HOLLOWELL •</text>
    <circle class="badge" cx="382" cy="702" r="28"/>
    <text class="brand-name" x="382" y="706" font-size="11">Hollowell</text>
    <text class="guarantee" x="382" y="737">LIFETIME</text>
    <text class="guarantee" x="382" y="745">GUARANTEE</text>
    <text class="product-name" x="382" y="778" font-size="13">Coffee Mug</text>
    <rect class="divider" x="364" y="786" width="36" height="3" rx="1.5" role="img" aria-label="Small scroll divider ornament"/>
    <ellipse class="ornament" cx="282" cy="667" rx="16" ry="8" role="img" aria-label="Corner flourish ornament"/>
    <ellipse class="ornament" cx="480" cy="667" rx="16" ry="8" role="img" aria-label="Corner flourish ornament"/>
    <ellipse class="ornament" cx="282" cy="786" rx="16" ry="8" role="img" aria-label="Corner flourish ornament"/>
    <ellipse class="ornament" cx="480" cy="786" rx="16" ry="8" role="img" aria-label="Corner flourish ornament"/>
  </g>

  <!-- right side panel -->
  <rect class="side-band" x="500" y="657" width="140" height="140"/>
  <text class="origin" x="508" y="774">MADE IN</text>
  <text class="origin" x="508" y="785">INDIA</text>
  <polygon class="board" points="500,797 640,797 640,838 612,865 500,865"/>

  <!-- back panel -->
  <g class="back-panel">
    <rect class="panel-face" x="640" y="657" width="240" height="140"/>
    <polygon class="panel-shade" points="790,797 880,730 880,797"/>
    <ellipse class="steam" cx="818" cy="708" rx="30" ry="42" role="img" aria-label="Faint rising steam decoration"/>
    <g class="cup-icon" aria-label="Steaming coffee cup icon">
      <path class="cup-steam" d="M760,695 q-4,-5 0,-10 q4,-5 0,-10"/>
      <path class="cup-steam" d="M768,697 q-4,-6 0,-12 q4,-6 0,-12"/>
      <path class="cup-body" d="M746,703 H782 L779,740 Q778,748 770,748 H758 Q750,748 749,740 Z"/>
      <path class="cup-handle" d="M781,710 Q793,710 792,721 Q791,731 779,732"/>
    </g>
    <text class="product-name" x="765" y="775" font-size="13">Coffee Mug</text>
    <ellipse class="ornament" cx="660" cy="667" rx="16" ry="8" role="img" aria-label="Corner flourish ornament"/>
    <ellipse class="ornament" cx="860" cy="667" rx="16" ry="8" role="img" aria-label="Corner flourish ornament"/>
    <ellipse class="ornament" cx="660" cy="786" rx="16" ry="8" role="img" aria-label="Corner flourish ornament"/>
    <ellipse class="ornament" cx="860" cy="786" rx="16" ry="8" role="img" aria-label="Corner flourish ornament"/>
  </g>

  <!-- glue tab -->
  <polygon class="board" points="880,657 900,672 900,788 880,800"/>

  <!-- bottom flap -->
  <path class="board" d="M640,797 L880,797 L880,942 Q880,950 872,950 L648,950 Q640,950 640,942 Z"/>

  <!-- fold lines -->
  <g class="folds">
    <line class="fold" x1="262" y1="657" x2="500" y2="657"/>
    <line class="fold" x1="122" y1="657" x2="262" y2="657"/>
    <line class="fold" x1="500" y1="657" x2="640" y2="657"/>
    <line class="fold" x1="122" y1="797" x2="262" y2="797"/>
    <line class="fold" x1="500" y1="797" x2="640" y2="797"/>
    <line class="fold" x1="640" y1="797" x2="880" y2="797"/>
    <line class="fold" x1="880" y1="657" x2="880" y2="800"/>
  </g>
</svg>
</body>
</html>
```